Spanish Student Needs a Cover for his PhD Dissertation

Hi everyone :) So, I'm a Corneal surgeon currently finishing my PhD, with a dissertation focused on the evaluation of quality of life in patients affected by a disease called Keratoconus. Just so you know, Keratoconus is a condition in which the cornea (the frontal part of the way) gets thin and bulgy and it decreases vision. What I did during my PhD was designing a questionnaire for evaluating quality of life in this kind of patients.
I need to design a hard cover for my dissertation, which is 200 sheets long. I like kind of minimalistic and geometric designs but I am totally open to suggestions. What needs to be in the cover is the name of the dissertation "Diseño, desarrollo y validación de una encuesta para evaluar el compromiso visual y emocional subjetivos en pacientes con Queratocono" and my name, "Iñigo Zabaleta". The other thing that needs to go there is the logo of my university (Universidad de Montealto). Aside from that, anything else is up to the designer. It would be important to use the kind of "red" color I am using in the dissertation. I am attaching the frontal page of my dissertation so you know what kind of design and colors I am using.
In the back part, of the cover, there should be this small inscription: "Iñigo Zabaleta, MD, es un Oftalmólogo Subespecialista en Cirugía Refractiva de la Universidad Católica Mirandina (Colombia) y la Universidad de Montealto (España). Actualmente se desempeña como miembro del Departamento de Córnea y Cirugía Refractiva de la Clínica de Oftalmología Los Robles y como director de su propia compañía de emprendimiento médico Silver Heron Surgical". Please leave a space to place my picture; I will have it taken this week so I don't have it right now, you can just leave the blank spot and I will include it later
The size of the pages is standard "letter" size.
Thanks a lot!

Target Market(s)

PhD Scholars

Font styles to use
Serif

Requirements
Must have
• The "red" color I use on my font. It must be formal but "young".
Nice to have
• I like to keep the design clean, kind of "formal with a young" touch so to speak. I really like gray colors, so it would be nice to have broad areas of gray. I love geometrical designs.
I have uploaded a very early version a friend of mine made (it even had a different title); this can be a starting point for you to work on, but I am more than open to suggestions and new ideas.
Should not have
• Please don't use my whole name, Iñigo Zabaleta is fine. I don't like ALL CAPITALS.

```html
<!DOCTYPE html>
<html lang="es">
<head>
<meta charset="utf-8">
<title>Tesis Doctoral — Iñigo Zabaleta</title>
<link href="https://fonts.googleapis.com/css2?family=Oswald:wght@500;600&family=Poppins:wght@300;400&display=swap" rel="stylesheet">
<style>
  :root {
    --slate: #2e323d;
    --slate-deep: #262a33;
    --crimson: #9b0f1e;
    --crimson-dark: #7d0a15;
    --crimson-light: #b3202e;
    --paper: #ffffff;
    --stage: #c9c9c9;
    --photo-light: #b8b8b8;
    --photo-dark: #3a3a3a;
    --placeholder: #a9a9ad;
  }
  * { box-sizing: border-box; margin: 0; padding: 0; }
  html, body { width: 1200px; height: 972px; overflow: hidden; }
  body { background: var(--stage); position: relative; font-family: "Poppins", sans-serif; }

  .cover {
    position: absolute; top: 136px; width: 540px; height: 700px;
    background: var(--slate); overflow: hidden;
  }
  .cover--front { left: 30px; }
  .cover--back { left: 588px; }
  .cover__art { position: absolute; inset: 0; width: 540px; height: 700px; }

  .front__label {
    position: absolute; left: 48px; top: 352px;
    font-weight: 300; font-size: 19px; color: var(--paper);
  }
  .front__title {
    position: absolute; left: 48px; top: 398px; width: 460px;
    border-left: 5px solid var(--paper); padding-left: 14px;
    font-family: "Oswald", sans-serif; font-weight: 600;
    font-size: 25px; line-height: 1.24; color: var(--paper);
    letter-spacing: -0.2px;
  }
  .front__title .accent { color: var(--crimson-light); }
  .front__author {
    position: absolute; left: 64px; top: 594px;
    font-family: "Oswald", sans-serif; font-weight: 600;
    font-size: 36px; color: var(--paper);
  }
  .front__university {
    position: absolute; right: 40px; top: 620px;
    display: flex; align-items: center; gap: 8px;
    font-family: "Poppins", sans-serif; font-weight: 400;
    font-size: 10.5px; color: var(--paper);
  }
  .front__university .dot {
    width: 26px; height: 26px; border-radius: 50%; background: var(--paper);
  }

  .back__bio {
    position: absolute; left: 58px; top: 262px; width: 390px;
    font-weight: 300; font-size: 13.4px; line-height: 1.62;
    color: var(--paper); text-align: justify; letter-spacing: 0.3px;
  }

  .spine {
    position: absolute; left: 1128px; top: 136px; width: 42px; height: 700px;
    background: linear-gradient(90deg, var(--crimson-dark), var(--crimson) 55%, var(--crimson-dark));
  }
  .spine__text {
    position: absolute; left: 50%; transform-origin: center;
    white-space: nowrap; color: var(--paper);
  }
  .spine__title {
    top: 220px; transform: translate(-50%, -50%) rotate(-90deg);
    font-family: "Oswald", sans-serif; font-weight: 600;
    font-size: 9.5px; line-height: 1.2; text-align: left;
  }
  .spine__author {
    top: 612px; transform: translate(-50%, -50%) rotate(-90deg);
    font-family: "Oswald", sans-serif; font-weight: 600; font-size: 22px;
  }
</style>
</head>
<body>

<section class="cover cover--front">
  <svg class="cover__art" viewBox="0 0 540 700" aria-hidden="false">
    <defs>
      <linearGradient id="eyePhoto" x1="0" y1="0" x2="1" y2="1">
        <stop offset="0" stop-color="#d9d9d9"/>
        <stop offset="0.45" stop-color="#7a7a7a"/>
        <stop offset="1" stop-color="#4a4a4a"/>
      </linearGradient>
      <radialGradient id="hexPhoto" cx="0.5" cy="0.5" r="0.6">
        <stop offset="0" stop-color="#4a4a4a"/>
        <stop offset="0.45" stop-color="#8c8c8c"/>
        <stop offset="1" stop-color="#c4c4c4"/>
      </radialGradient>
      <linearGradient id="gloss" x1="0" y1="0" x2="1" y2="0">
        <stop offset="0" stop-color="#ffffff" stop-opacity="0"/>
        <stop offset="1" stop-color="#ffffff" stop-opacity="0.45"/>
      </linearGradient>
    </defs>
    <polygon class="band band--left" points="0,105 290,300 0,380" fill="var(--crimson-light)"/>
    <polygon class="band band--right" points="540,100 300,300 540,490" fill="var(--crimson)"/>
    <polygon class="gloss" points="0,330 60,290 100,320 0,390" fill="url(#gloss)" opacity="0.5"/>
    <polygon class="gloss" points="540,380 460,320 420,360 540,450" fill="url(#gloss)" opacity="0.5"/>
    <polygon class="photo-eye" points="0,0 540,0 540,100 300,300 0,105" fill="url(#eyePhoto)"
      role="img" aria-label="Fotografía en blanco y negro de un ojo en primer plano"/>
    <polygon class="photo-hex" points="280,152 339,186 339,254 280,288 221,254 221,186"
      fill="url(#hexPhoto)" stroke="var(--paper)" stroke-width="7"
      role="img" aria-label="Fotografía de un ojo, nítida"/>
    <polygon class="photo-hex" points="408,152 467,186 467,254 408,288 349,254 349,186"
      fill="url(#hexPhoto)" stroke="var(--paper)" stroke-width="7"
      role="img" aria-label="Fotografía de un ojo, algo desenfocada"/>
    <polygon class="photo-hex" points="344,262 403,296 403,364 344,398 285,364 285,296"
      fill="url(#hexPhoto)" stroke="var(--paper)" stroke-width="7"
      role="img" aria-label="Fotografía de un ojo, muy desenfocada"/>
  </svg>

  <p class="front__label">Tesis Doctoral</p>
  <h1 class="front__title">
    Diseño, desarrollo y validación de una<br>
    encuesta para evaluar el compromiso visual<br>
    y emocional subjetivos en pacientes con<br>
    <span class="accent">Queratocono</span>
  </h1>
  <p class="front__author">Iñigo Zabaleta</p>
  <div class="front__university">
    <span class="dot"></span>
    <span>Universidad de Montealto</span>
  </div>
</section>

<section class="cover cover--back">
  <svg class="cover__art" viewBox="0 0 540 700">
    <defs>
      <linearGradient id="glossBack" x1="0" y1="0" x2="1" y2="0">
        <stop offset="0" stop-color="#ffffff" stop-opacity="0"/>
        <stop offset="1" stop-color="#ffffff" stop-opacity="0.45"/>
      </linearGradient>
    </defs>
    <polygon class="band" points="0,30 120,105 0,180" fill="var(--crimson-light)"/>
    <polygon class="band" points="455,0 540,0 540,58" fill="var(--crimson)"/>
    <polygon class="band" points="540,440 118,692 400,632 540,700" fill="var(--crimson)"/>
    <polygon class="gloss" points="540,500 470,550 500,580 540,560" fill="url(#glossBack)" opacity="0.6"/>
    <ellipse class="portrait-slot" cx="246" cy="152" rx="53" ry="65" fill="var(--placeholder)"
      role="img" aria-label="Espacio reservado para la fotografía del autor"/>
  </svg>

  <p class="back__bio">
    Iñigo Zabaleta, MD, es un Oftalmólogo Subespecialista en Cirugía Refractiva de la Universidad Católica Mirandina (Colombia) y la Universidad de Montealto (España).<br>
    Actualmente se desempeña como miembro del Departamento de Córnea y Cirugía Refractiva de la Clínica de Oftalmología Los Robles y como director de su propia compañía de emprendimiento médico Silver Heron Surgical.
  </p>
</section>

<aside class="spine">
  <p class="spine__text spine__title">
    Diseño, desarrollo y validación de una encuesta para evaluar el compromiso<br>
    visual y emocional subjetivos en pacientes con Queratocono
  </p>
  <p class="spine__text spine__author">Iñigo Zabaleta</p>
</aside>

</body>
</html>
```